Name Card Design

Looking to create a card for my business. I am a personal stylist, my business is clothes, shoes and everything to do with looking fashion forward. I help people achieve the most polished look with cloths and grooming. I would like my card to be a reflection of my qualities which are: poise, elegance, creativity and fairness.
Things I like a simple yet expensive looking, sometimes less simple but highly creative and different catches my eye. For instance I saw a card with lace trimming at the bottom, it made me think about the business that person was in. I don't like childish designs with butterflies, trees, flowers, etc.
Here is my site www.Marta-Venn.example for your perusal

On the card it should have the following info
Marta Venn
personal stylist
www.Marta-Venn.example
(+65) 842-30587
Facebook page: Ringtochic

Back of the card:
Wardrobe weeding
Personal shopping
Style consultation

Target Market(s)

mostly working women

Industry/Entity Type

Fashion

Font styles to use
Serif
Sans Serif

Requirements
Should not have
• butterflies, flowers, feathers, etc

```html
<!DOCTYPE html>
<html lang="en">
<head>
<meta charset="utf-8">
<title>Marta Venn – Personal Stylist Business Card</title>
<link rel="stylesheet" href="https://fonts.googleapis.com/css2?family=Barlow:wght@400;500&family=Arimo:wght@400;700&display=swap">
<style>
  :root {
    --backdrop: #e9e6e2;
    --card-light: #ececec;
    --card-dark: #1e1e1e;
    --ink: #2a2a2a;
    --accent: #c8171d;
    --monogram: #e0e0e0;
    --emboss: #151515;
  }
  html, body {
    margin: 0;
    width: 1200px;
    height: 900px;
    overflow: hidden;
    background: var(--backdrop);
  }
  .canvas {
    position: relative;
    width: 1200px;
    height: 900px;
  }
  .card {
    position: absolute;
    left: 354px;
    width: 488px;
    height: 279px;
    box-shadow: 0 2px 4px rgba(0,0,0,0.25);
  }
  .card--front {
    top: 153px;
    background: var(--card-light);
    font-family: "Barlow", sans-serif;
    color: var(--ink);
  }
  .card--back {
    top: 463px;
    background: var(--card-dark);
  }
  .marker {
    position: absolute;
    left: 33px;
    top: 60px;
    width: 9px;
    height: 9px;
    border-radius: 50%;
    background: var(--accent);
  }
  .identity {
    position: absolute;
    left: 65px;
    top: 50px;
    margin: 0;
    white-space: nowrap;
  }
  .identity__name {
    font-size: 21px;
    font-weight: 400;
    letter-spacing: 0.3px;
  }
  .identity__role {
    font-size: 14px;
    color: var(--accent);
    letter-spacing: 0.4px;
    margin-left: 4px;
  }
  .contacts {
    position: absolute;
    left: 65px;
    top: 123px;
    margin: 0;
  }
  .contacts dt {
    font-size: 11.5px;
    font-weight: 500;
    line-height: 14px;
  }
  .contacts dd {
    margin: 0 0 11px;
    font-size: 14.5px;
    line-height: 18px;
    letter-spacing: 0.6px;
  }
  .monogram {
    position: absolute;
    right: 48px;
    top: 140px;
    font-family: "Arimo", sans-serif;
    font-weight: 700;
    font-size: 96px;
    line-height: 1;
    letter-spacing: -6px;
    color: var(--monogram);
  }
  .back-name {
    position: absolute;
    left: 0;
    right: 0;
    top: 102px;
    text-align: center;
    font-family: "Arimo", sans-serif;
    font-weight: 700;
    font-size: 72px;
    line-height: 1;
    letter-spacing: -3px;
    color: var(--emboss);
    text-shadow: 0 1px 0 rgba(255,255,255,0.03);
  }
  .services {
    position: absolute;
    left: 0;
    right: 0;
    top: 171px;
    text-align: center;
    font-family: "Arimo", sans-serif;
    font-size: 12.5px;
    color: var(--accent);
    margin: 0;
  }
</style>
</head>
<body>
<main class="canvas">
  <section class="card card--front" aria-label="Card front">
    <span class="marker"></span>
    <h1 class="identity">
      <span class="identity__name">Marta Venn</span>
      <span class="identity__role">PERSONAL STYLIST</span>
    </h1>
    <dl class="contacts">
      <dt>telephone</dt>
      <dd>(+65) 842-30587</dd>
      <dt>website</dt>
      <dd>www.marta-venn.example</dd>
      <dt>facebook</dt>
      <dd>/ringtochic</dd>
    </dl>
    <div class="monogram" aria-hidden="true">MV</div>
  </section>

  <section class="card card--back" aria-label="Card back">
    <div class="back-name">Marta Venn</div>
    <p class="services">Wardrobe weeding | Personal style advice | Private shopping</p>
  </section>
</main>
</body>
</html>
```